LA's Newest HEMP Facial Oil and Body Oil Packaging Project

We need a packaging concept for a Hemp based facial oil and body oil. We need label design for the bottle and carton graphics. I am attaching a few reference photos. The target demographic is women between 17-35 year old. Products need to be able to stand out in crowded stores with clear calls to action.
1oz Dropper Bottle with Unit Carton - Hemp Facial Oil
4oz PET Bottle with Unit Carton - Hemp + Rose Facial Oil

```html
<!DOCTYPE html>
<html lang="en">
<head>
<meta charset="utf-8">
<title>Hemp Face Oil – Carton and Label</title>
<link href="https://fonts.googleapis.com/css2?family=Bevan&family=Sacramento&family=Josefin+Sans:wght@400;700&display=swap" rel="stylesheet">
<style>
  :root {
    --backdrop: #4a4a3b;
    --olive: #555a42;
    --olive-dark: #3f4432;
    --paper: #e8e4e2;
    --ink: #4b4a3c;
    --rose-red: #d8243e;
    --gold-light: #f6e7b6;
    --gold-mid: #e2c67e;
    --gold-deep: #c9a458;
    --cream-text: #f1eee6;
    --leaf-green: #3f6a3e;
    --rose-pink: #d9577a;
  }
  * { box-sizing: border-box; margin: 0; padding: 0; }
  html, body { width: 1200px; height: 900px; overflow: hidden; }
  body { background: var(--backdrop); position: relative; font-family: "Josefin Sans", sans-serif; }

  .carton { position: absolute; left: 170px; top: 80px; height: 740px; display: flex; }
  .carton-side, .carton-front { position: relative; height: 100%; display: flex; flex-direction: column; }
  .carton-side { width: 100px; }
  .carton-front { width: 310px; }

  .floral-art {
    height: 205px;
    background: linear-gradient(135deg, var(--gold-light) 0%, var(--leaf-green) 40%, var(--rose-pink) 70%, var(--gold-mid) 100%);
  }
  .white-panel { flex: 1; background: var(--paper); position: relative; }
  .gold-band {
    background: linear-gradient(90deg, var(--gold-mid), var(--gold-light) 45%, var(--gold-mid) 75%, var(--gold-deep));
  }
  .green-base { background: var(--olive); color: var(--cream-text); text-align: center; }

  .carton-side .white-panel { display: flex; align-items: flex-start; justify-content: center; padding-top: 20px; }
  .ingredients {
    writing-mode: vertical-rl;
    display: flex; gap: 6px; align-items: center;
    color: var(--ink);
  }
  .ingredients-title { font-family: "Josefin Sans", sans-serif; font-weight: 700; font-size: 15px; letter-spacing: 1.5px; }
  .ingredients-list { font-family: "Sacramento", cursive; font-size: 20px; }
  .carton-side .gold-band { height: 85px; }
  .carton-side .green-base { height: 140px; }
  .carton-side .floral-art { filter: brightness(0.85); }

  .product-name { text-align: center; color: var(--ink); }
  .product-title { font-family: "Bevan", serif; letter-spacing: 3px; line-height: 1; }
  .product-sub { font-family: "Sacramento", cursive; line-height: 1; }
  .leaf-art {
    display: block; margin: 0 auto;
    background: radial-gradient(circle at 50% 55%, #b9b6ae 0%, #d6d3cf 55%, var(--paper) 75%);
    border-radius: 50%;
  }
  .tagline { font-family: "Sacramento", cursive; color: var(--rose-red); text-align: center; }
  .skin-types { font-weight: 700; letter-spacing: 1.5px; }
  .volume { font-weight: 400; letter-spacing: 1px; }

  .carton-front .white-panel { padding-top: 58px; }
  .carton-front .product-title { font-size: 52px; }
  .carton-front .product-sub { font-size: 44px; margin-top: 4px; }
  .carton-front .leaf-art { width: 120px; height: 130px; margin-top: 40px; }
  .carton-front .gold-band { height: 85px; display: flex; align-items: center; justify-content: center; }
  .carton-front .tagline { font-size: 32px; }
  .carton-front .green-base { height: 140px; padding-top: 50px; }
  .carton-front .skin-types { font-size: 22px; }
  .carton-front .volume { font-size: 16px; margin-top: 16px; }

  .bottle-label {
    position: absolute; left: 680px; top: 240px; width: 380px; height: 420px;
    display: flex; flex-direction: column;
  }
  .bottle-label .white-panel { padding-top: 42px; }
  .bottle-label .product-title { font-size: 46px; }
  .bottle-label .product-sub { font-size: 38px; margin-top: 2px; }
  .bottle-label .leaf-art { width: 110px; height: 115px; margin-top: 22px; }
  .bottle-label .gold-band { height: 56px; display: flex; align-items: center; justify-content: center; }
  .bottle-label .tagline { font-size: 28px; }
  .bottle-label .green-base { height: 95px; padding-top: 32px; }
  .bottle-label .skin-types { font-size: 17px; }
  .bottle-label .volume { font-size: 13px; margin-top: 10px; }
</style>
</head>
<body>
  <section class="carton" aria-label="Unit carton artwork">
    <div class="carton-side">
      <div class="floral-art" role="img" aria-label="Illustration of hemp leaves and pink roses on gold"></div>
      <div class="white-panel">
        <div class="ingredients">
          <span class="ingredients-title">INGREDIENTS</span>
          <span class="ingredients-list">Hemp oil and rose</span>
        </div>
      </div>
      <div class="gold-band"></div>
      <div class="green-base"></div>
    </div>
    <div class="carton-front">
      <div class="floral-art" role="img" aria-label="Illustration of hemp leaves and pink roses on gold"></div>
      <div class="white-panel">
        <div class="product-name">
          <h1 class="product-title">HEMP</h1>
          <p class="product-sub">Face Oil</p>
        </div>
        <div class="leaf-art" role="img" aria-label="Engraved hemp leaf illustration"></div>
      </div>
      <div class="gold-band"><p class="tagline">Hemp oil and rose</p></div>
      <div class="green-base">
        <p class="skin-types">ALL SKIN TYPES</p>
        <p class="volume">1OZ 30ML</p>
      </div>
    </div>
  </section>

  <section class="bottle-label" aria-label="Dropper bottle label artwork">
    <div class="white-panel">
      <div class="product-name">
        <h2 class="product-title">HEMP</h2>
        <p class="product-sub">Face Oil</p>
      </div>
      <div class="leaf-art" role="img" aria-label="Engraved hemp leaf illustration"></div>
    </div>
    <div class="gold-band"><p class="tagline">Hemp oil and rose</p></div>
    <div class="green-base">
      <p class="skin-types">ALL SKIN TYPES</p>
      <p class="volume">1OZ 30ML</p>
    </div>
  </section>
</body>
</html>
```